Word Doc Report NEED THIS OVERNIGHT!

I have a design ready, I need someone to take a report that we have, and input it in to the design that has been created. The final product needs to be delivered in Word.
The file called "Sketch Forge" is the design concept we need to use
The file called "7 Elmwick Lane" is all of the data that needs to be put into the word doc based on the elements in the Sketch Forge file.

```html
<!DOCTYPE html>
<html lang="en">
<head>
<meta charset="utf-8">
<title>ACT Maintenance Plan – Report Pages</title>
<link rel="stylesheet" href="https://fonts.googleapis.com/css2?family=Carlito:ital,wght@0,400;0,700;1,400;1,700&family=Exo+2:ital,wght@1,800&family=Montserrat:wght@400;600&display=swap">
<style>
:root{
  --backdrop:#e8e8e8;
  --paper:#ffffff;
  --teal:#17a897;
  --teal-dark:#0b5a5f;
  --green-light:#a5d36a;
  --sky:#1a9bd7;
  --navy:#2d5f95;
  --ink:#222;
  --table-head:#4472c4;
  --row-light:#dae3f3;
  --row-mid:#c5d4ee;
  --tick:#17a897;
  --note-blue:#dde9f3;
  --note-green:#e2efd9;
}
*{box-sizing:border-box;margin:0;padding:0}
html,body{width:1200px;height:727px;overflow:hidden;background:var(--backdrop)}
body{font-family:"Carlito",Calibri,sans-serif;color:var(--ink)}
.stage{position:absolute;left:0;top:0;width:2464px;height:1492px;transform:scale(0.48701);transform-origin:0 0}
.page{position:absolute;background:var(--paper);overflow:hidden}
.abs{position:absolute}

/* cover */
.cover{left:338px;top:63px;width:530px;height:749px}
.cover-shapes{position:absolute;left:0;top:0}
.brand-name{position:absolute;left:290px;top:95px;width:200px;font-family:"Montserrat",sans-serif;font-weight:600;color:var(--navy);font-size:31px;line-height:36px;text-align:right}
.cover-rule{left:199px;top:167px;width:331px;height:10px;background:var(--sky)}
.cover-photo{left:150px;top:182px;width:380px;height:280px;background:linear-gradient(180deg,#6f9cc9 0%,#a9c3dc 45%,#c8b49a 70%,#6a5a3c 100%)}
.cover-title{left:20px;top:430px;width:224px;text-align:center;font-family:"Exo 2",sans-serif;font-style:italic;font-weight:800;color:#fff;font-size:31px;line-height:34px}
.cover-title .date{display:block;font-size:14px;line-height:22px}
.plan-label{left:270px;top:490px;width:258px;text-align:center;font-family:"Montserrat",sans-serif;color:#fff}
.plan-label strong{display:block;font-size:16px;font-weight:600}
.plan-label span{display:block;font-size:12.5px;margin-top:3px}
.contact-row{left:252px;display:flex;align-items:flex-start;gap:16px;font-family:"Montserrat",sans-serif;font-size:11px;color:#222;line-height:13px}
.contact-icon{width:22px;height:22px;border-radius:50%;background:var(--teal);flex:none;display:flex;align-items:center;justify-content:center}

/* shared headers / footers */
.page-foot{position:absolute;left:0;bottom:0;width:100%;height:48px}
.page-foot .bar{position:absolute;left:30px;right:0;bottom:0;height:20px;background:var(--teal);color:#fff;font-weight:700;font-size:7px;line-height:20px;padding-left:20px}
.page-foot svg{position:absolute;left:0;bottom:0}
.section-bar{position:absolute;height:20px;background:var(--sky);color:#fff;font-weight:700;font-size:13.5px;line-height:20px;padding-left:3px}

/* summary page */
.summary{left:932px;top:63px;width:530px;height:749px}
.summary-head{left:42px;top:20px;width:488px;height:27px;background:var(--teal);color:#fff;font-weight:700;font-size:19px;line-height:27px;padding-left:23px}
.fact-table{left:38px;top:62px;width:468px;border-collapse:collapse;font-size:8px}
.fact-table td{height:14.2px;padding:0 5px;border-bottom:1px solid #fff}
.fact-table .label{width:153px;background:var(--table-head);color:#fff;font-weight:700}
.fact-table .value{background:var(--row-light)}
.fact-table tr:nth-child(even) .value{background:var(--row-mid)}
.summary-body{left:38px;top:211px;width:456px;font-size:8.3px;line-height:12px;text-align:justify}
.summary-body p{margin-bottom:7px}
.summary-body ul{list-style:none;margin:2px 0 2px 16px}
.summary-body li::before{content:"•";color:var(--teal);margin-right:10px}
.important{color:#333;font-style:italic}
.important b.tag{color:var(--sky);font-style:normal}
.signature-area{left:38px;top:640px;width:130px;height:26px;background:#f1f1f1}
.signer{left:38px;top:671px;color:var(--sky);font-size:10.5px;line-height:12px}

/* partners page */
.partners{left:1525px;top:63px;width:530px;height:749px}
.charity-name{left:50px;top:92px;font-size:27px;font-weight:700;color:var(--teal)}
.badge-pest{left:223px;top:63px;width:140px;height:58px;background:#3d8b3d;border-radius:3px}
.badge-builders{left:398px;top:45px;width:60px;height:60px;background:#e88a24}
.note-blue{left:47px;top:149px;width:434px;height:27px;background:var(--note-blue);font-size:6px;line-height:7.5px;padding:4px 6px;color:#444}
.note-green{left:47px;top:182px;width:434px;height:33px;background:var(--note-green);font-size:8.3px;line-height:12px;padding:4px 6px;font-style:italic}
.map-street{left:67px;top:227px;width:398px;height:208px;background:linear-gradient(135deg,#cfe6c6 0%,#e7efe2 45%,#9cc9e8 60%,#d7e8cf 100%)}
.map-aerial{left:67px;top:454px;width:398px;height:230px;background:linear-gradient(135deg,#4f5a4b 0%,#7d8377 50%,#5d6b52 100%)}

/* observation / action / esl tables */
.wide-page{top:884px;width:750px;height:529px}
.intro{position:absolute;font-size:7.2px;line-height:10.5px;text-align:justify}
.data-table{position:absolute;border-collapse:collapse;font-size:6.6px;table-layout:fixed}
.data-table th{background:var(--table-head);color:#fff;text-align:left;font-weight:700;padding:0 3px}
.data-table td{padding:0 3px;vertical-align:top;border-right:1px solid #c9d3e4}
.data-table tbody tr:nth-child(odd) td{background:#fff}
.data-table tbody tr:nth-child(even) td{background:#e3eaf6}
.data-table td.area{font-weight:700}
.obs th,.obs td{line-height:9.6px;padding-top:1.6px;padding-bottom:1.6px}
.act th,.act td{line-height:8.6px;padding-top:1.1px;padding-bottom:1.1px}

.esl{left:37px;top:38px;width:673px;font-size:8.2px;font-family:"Montserrat",sans-serif;font-weight:400;color:#333}
.esl th{background:#cfe2f3;font-weight:400;padding:1px 3px;line-height:10px}
.esl .caption th{background:#9dc3e6;color:#fff;text-align:left;font-size:8px;line-height:10px;padding:1px 4px}
.esl td{border:1px solid #d4dce8;padding:0 3px;line-height:10.5px;background:#fff}
.esl td.num{text-align:center}
.esl .tick{display:inline-block;width:7px;height:7px;border:1px solid var(--tick);position:relative}
.esl .tick::after{content:"";position:absolute;left:1.5px;top:0;width:2px;height:4px;border:solid var(--tick);border-width:0 1px 1px 0;transform:rotate(45deg)}
</style>
</head>
<body>
<div class="stage">

  <!-- Cover -->
  <section class="page cover">
    <svg class="cover-shapes" width="530" height="749" viewBox="0 0 530 749" aria-hidden="true">
      <polygon points="75,82 210,217 75,352 0,277 0,157" fill="var(--green-light)"/>
      <polygon points="0,240 60,300 0,360" fill="var(--teal)"/>
      <polygon points="70,280 130,340 70,400 10,340" fill="var(--green-light)"/>
      <polygon points="30,360 75,405 30,450 0,420 0,390" fill="var(--green-light)"/>
    </svg>
    <div class="brand-name">Homestead<br>Reports</div>
    <div class="abs cover-rule"></div>
    <div class="abs cover-photo" role="img" aria-label="Photo of a modern apartment building at dusk with trees in front"></div>
    <svg class="cover-shapes" width="530" height="749" viewBox="0 0 530 749" aria-hidden="true">
      <polygon points="127,127 230,222 127,317 30,222" fill="var(--teal-dark)"/>
      <polygon points="127,342 277,492 127,642 0,515 0,469" fill="var(--teal)"/>
      <polygon points="287,477 530,477 530,544 247,544" fill="var(--sky)"/>
      <polygon points="0,705 262,705 238,749 0,749" fill="var(--navy)"/>
      <polygon points="268,705 530,705 530,749 244,749" fill="var(--teal)"/>
    </svg>
    <div class="abs cover-title">ACT<br>Maintenance<br>Plan<span class="date">2 May 2022</span></div>
    <div class="abs plan-label"><strong>Units Plan 1722</strong><span>7 Elmwick Lane Canberra City</span></div>
    <div class="abs contact-row" style="top:576px">
      <span class="contact-icon"><svg width="12" height="12" viewBox="0 0 12 12"><path d="M1 5l5-3 5 3v6H1z" fill="none" stroke="#fff" stroke-width="1.3"/></svg></span>
      <span style="padding-top:4px">hello@homesteadreports.com.au</span>
    </div>
    <div class="abs contact-row" style="top:610px">
      <span class="contact-icon"><svg width="12" height="12" viewBox="0 0 12 12"><circle cx="6" cy="6" r="5" fill="none" stroke="#fff" stroke-width="1.2"/><path d="M1 6h10M6 1v10" stroke="#fff" stroke-width="1"/></svg></span>
      <span style="padding-top:4px">homesteadreports.com.au</span>
    </div>
    <div class="abs contact-row" style="top:644px">
      <span class="contact-icon"><svg width="12" height="12" viewBox="0 0 12 12"><path d="M1 6l5-5 5 5M2.5 5v6h7V5" fill="none" stroke="#fff" stroke-width="1.3"/></svg></span>
      <span style="padding-top:4px">18 Larkfield Road, Hughes ACT 2605<br>p 6211 4870</span>
    </div>
  </section>

  <!-- Report summary -->
  <section class="page summary">
    <svg class="abs" style="left:0;top:8px" width="48" height="52" viewBox="0 0 48 52" aria-hidden="true">
      <polygon points="12,0 24,12 12,24 0,12" fill="var(--green-light)"/>
      <polygon points="24,10 42,28 24,46 6,28" fill="var(--teal-dark)"/>
      <polygon points="8,34 16,42 8,50 0,42" fill="var(--green-light)"/>
    </svg>
    <div class="abs summary-head">REPORT SUMMARY</div>
    <table class="abs fact-table">
      <tr><td class="label">CLIENT</td><td class="value">Crestline Strata Pty Ltd</td></tr>
      <tr><td class="label">BUILDING LOCATION</td><td class="value">7 Elmwick Lane Canberra City ACT</td></tr>
      <tr><td class="label">BLOCK NUMBER</td><td class="value">13</td></tr>
      <tr><td class="label">SECTION NUMBER</td><td class="value">12</td></tr>
      <tr><td class="label">SCHEME NUMBER</td><td class="value">UP1722</td></tr>
      <tr><td class="label"></td><td class="value"></td></tr>
      <tr><td class="label">INSPECTION DATE</td><td class="value">2 May 2022</td></tr>
      <tr><td class="label">INSPECTOR</td><td class="value">Lena Harcourt</td></tr>
      <tr><td class="label">WEATHER CONDITIONS</td><td class="value">Fine</td></tr>
      <tr><td class="label">REFERENCE NUMBER</td><td class="value">35TST</td></tr>
    </table>
    <div class="abs summary-body">
      <p style="margin-bottom:2px"><b><i>Project Scope:</i></b> This Maintenance Plan has been compiled to assist the Owners Corporation and Strata Managers to meet their obligations with respect to the following legislation (both as amended 1 November 2020):</p>
      <ul><li>Unit Titles (Management) Act 2011 (s24);</li><li style="margin-top:3px">Unit Titles (Management) Regulation 2011 (s4A)</li></ul>
      <p style="margin:3px 0 0"><b><i>Building Class</i></b></p>
      <p style="margin-left:0">&nbsp;• Residential Units are Class A</p>
      <p>In typical Class A Units Plans, the unit owner owns the inside of the unit but not the main structure of the building. Usually, the individual owner owns from the inside of their lot to halfway out through the boundary walls, ceiling, and the floor. In general, the Owners Corporation owns the walls, ceiling and floor from outside of the lot to halfway in. The internal walls within the unit (e.g. the wall between the kitchen and lounge room), floor coverings, light fittings and curtains are all the property of the unit owner.</p>
      <p>The Unit Titles (Management) Act 2011 and associated regulations provides the framework for the management of multi-unit residential properties. All Owners Corporations are required to hold a Maintenance Plan, considering the Developers Maintenance Schedule (if available). The Executive Committee then references this plan as part of their responsibility for overseeing the maintenance of the common property. The Owners Corporation should regularly review their maintenance plan and amend when necessary. A comprehensive database relating to the maintenance, repair or replacement undertaken to systems, equipment, structures and other items on the common property, including copies of manuals and warranties (where available) has been compiled for this building.</p>
      <p>Following the preparation of our project file for 7 Elmwick Lane Canberra which included referencing materials such as maintenance schedules, sinking fund reports, warranties, manufacturer’s recommendations, and specific product information provided to us, our Building Inspector conducted a comprehensive on-site visual inspection on 2 May 2022. It is critical that this Maintenance Plan is monitored and updated on an ongoing basis to ensure the optimum working condition of systems, equipment, structures and other elements of the common property and to avoid costly reactive repairs.</p>
      <p class="important"><b class="tag">IMPORTANT:</b> This report is intended to be read in its entirety. It has been commissioned to satisfy the requirements of 4A Maintenance plan – Act, s 24 (3), Unit Titles Management Regulation 2011. The appropriate Strata Group Representative or Members of the Body Corporate Executive are requested to immediately contact our company if any of the report’s content is not fully understood and requires clarification or further explanation.<br><b>Please refer to important Scope and Limitations at the end of this document.</b></p>
      <p>Thank you for the opportunity to work with you on this project, please do not hesitate to contact our team.</p>
    </div>
    <div class="abs signature-area" role="img" aria-label="Inspector's handwritten signature"></div>
    <div class="abs signer">Lena Harcourt<br>Senior Building Inspector</div>
  </section>

  <!-- Partners and location -->
  <section class="page partners">
    <div class="abs charity-name">Open Door Fund</div>
    <div class="abs badge-pest"></div>
    <div class="abs badge-builders"></div>
    <div class="abs note-blue">A percentage from every inspection contributes to our in house charity, supporting those in our community who do not have a place to call home. Visit our website to learn more.</div>
    <div class="abs note-green">A comprehensive photo log of all photographs and documents captured during the maintenance plan inspection on 2 May 2022 have been supplied with this report.</div>
    <div class="abs map-street" role="img" aria-label="Street map of central Canberra with the building location circled"></div>
    <div class="abs map-aerial" role="img" aria-label="Aerial satellite view of the city block with the building circled"></div>
    <footer class="page-foot">
      <svg width="48" height="48" viewBox="0 0 48 48" aria-hidden="true">
        <polygon points="12,6 24,18 12,30 0,18" fill="var(--green-light)"/>
        <polygon points="24,10 40,26 24,42 8,26" fill="var(--teal-dark)"/>
        <polygon points="10,32 18,40 10,48 2,40" fill="var(--green-light)"/>
      </svg>
      <div class="bar">7 Elmwick Lane Canberra City - COPYRIGHT: Homestead Reports</div>
    </footer>
  </section>

  <!-- General observations -->
  <section class="page wide-page" style="left:45px">
    <div class="section-bar" style="left:35px;top:41px;width:677px">General Observations Summary</div>
    <p class="intro" style="left:37px;top:68px;width:674px">The preparation of this Maintenance Plan included a comprehensive on-site inspection where building elements noted in the plan were reviewed to determine life cycles and continuity of service. Whilst the purpose of a maintenance plan is not to specifically address defects, any observations noted by the inspector have been provided below as a courtesy. Please note that we cannot guarantee all defects to this structure have been listed and strongly recommend that the Routine/Safety inspections for each building element detailed in the plan are strictly observed. <b><i>Please refer to our Scope &amp; Limitations at the end of this document.</i></b></p>
    <table class="data-table obs" style="left:37px;top:121px;width:675px">
      <colgroup><col style="width:108px"><col style="width:109px"><col></colgroup>
      <thead><tr><th>Area</th><th>Observation</th><th>Details</th></tr></thead>
      <tbody>
        <tr><td class="area">Superstructure</td><td>Maintenance</td><td>Exterior of building adjacent to gymnasium requires painting</td></tr>
        <tr><td></td><td>Maintenance</td><td>Exterior of building adjacent to guest recreation room requires repainting</td></tr>
        <tr><td></td><td>Observation</td><td>Brightcoat paint observed in basement, clearly used for some external surfaces, but not a full building repaint</td></tr>
        <tr><td></td><td>Maintenance</td><td>Flaking paint was observed to balcony ceilings below the old pool area</td></tr>
        <tr><td></td><td>Maintenance</td><td>The window sill to a window adjacent to the outdoor recreation areas has deteriorated and requires repairs or replacement</td></tr>
        <tr><td></td><td>Maintenance</td><td>Some areas of foyer floor tiling require grout repairs</td></tr>
        <tr><td class="area">Garage Door</td><td>Observation</td><td>Observed servicemen at the building during our inspection</td></tr>
        <tr><td class="area">Basement line marking</td><td>Observation</td><td>There is varying levels of deterioration of lines, touch-ups to some areas is advised</td></tr>
        <tr><td class="area">Rooftop recreation area adjacent to tennis court</td><td>Landscaping</td><td>Rooftop recreation area requires weeding/spraying</td></tr>
        <tr><td class="area">Outdoor furniture</td><td>Maintenance/Replacement</td><td>Outdoor furniture adjacent to tennis court generally affected by weather. Serviceable. Would recommend outdoor cover if replaced.</td></tr>
        <tr><td class="area">Gym and public washrooms</td><td>Maintenance</td><td>There are some damaged ceiling tiles</td></tr>
        <tr><td class="area">Hallways</td><td>Maintenance</td><td>Patch painting, scuffing and impact damage was noted to some areas</td></tr>
        <tr><td class="area">Recreation room</td><td>Maintenance</td><td>Paint bubbling on some walls</td></tr>
        <tr><td class="area">Recreation room</td><td>Maintenance</td><td>The door handle to the recreation room is loose and requires repairs</td></tr>
        <tr><td class="area">Cooling tower</td><td>Maintenance</td><td>There is efflorescence present to a condenser pump from water leakage</td></tr>
        <tr><td class="area">Recreation deck</td><td>Structural defect/Hazard</td><td>The timber deck requires repairs and is structurally unsound</td></tr>
        <tr><td class="area">Stairwell</td><td>Maintenance</td><td>There are chipped and cracked tiles to the stairwell in some areas</td></tr>
        <tr><td class="area">Washroom</td><td>Maintenance</td><td>There are some damaged ceiling tiles</td></tr>
        <tr><td class="area">Sewer pump</td><td>Maintenance</td><td>Backflow prevention last tested 2014</td></tr>
        <tr><td class="area">Tennis court</td><td>Maintenance</td><td>Water was holding to areas of the court surface, drainage maintenance is recommended</td></tr>
      </tbody>
    </table>
    <footer class="page-foot">
      <svg width="48" height="48" viewBox="0 0 48 48" aria-hidden="true">
        <polygon points="12,6 24,18 12,30 0,18" fill="var(--green-light)"/>
        <polygon points="24,10 40,26 24,42 8,26" fill="var(--teal-dark)"/>
        <polygon points="10,32 18,40 10,48 2,40" fill="var(--green-light)"/>
      </svg>
      <div class="bar">7 Elmwick Lane Canberra City - COPYRIGHT: Homestead Reports</div>
    </footer>
  </section>

  <!-- Next action plan -->
  <section class="page wide-page" style="left:838px">
    <div class="section-bar" style="left:37px;top:39px;width:675px">Next Action Plan</div>
    <p class="intro" style="left:38px;top:68px;width:674px;font-size:8.2px">To assist with future planning, inspections recommended over the next 18 months are detailed below:</p>
    <table class="data-table act" style="left:38px;top:93px;width:674px">
      <colgroup><col style="width:222px"><col style="width:110px"><col style="width:120px"><col></colgroup>
      <thead><tr><th>Building Element</th><th>Type</th><th>Last Inspector</th><th>Next Inspection Due</th></tr></thead>
      <tbody>
        <tr><td class="area">Superstructure</td><td>Routine</td><td>Homestead Reports</td><td>May 2023</td></tr>
        <tr><td class="area">Basement/Car Accommodation</td><td>Routine</td><td>Homestead Reports</td><td>May 2023</td></tr>
        <tr><td class="area">Cleaning/Sanitation</td><td>Sanitation</td><td>CleanCo</td><td></td></tr>
        <tr><td class="area">Driveways, Pathways &amp; Parking</td><td>Routine</td><td>Homestead Reports</td><td>May 2023</td></tr>
        <tr><td class="area">Electrical &amp; Security</td><td>Operational</td><td>Voltline</td><td></td></tr>
        <tr><td class="area">External Works</td><td>Routine</td><td>Homestead Reports</td><td>May 2023</td></tr>
        <tr><td class="area">Fire Protection Systems &amp; Evacuation</td><td>Routine/Safety</td><td>FireSafe</td><td>September 2023</td></tr>
        <tr><td class="area">Furniture &amp; Fittings</td><td>Routine</td><td>Homestead Reports</td><td>May 2023</td></tr>
        <tr><td class="area">Gymnasium</td><td>Routine</td><td>Homestead Reports</td><td>May 2023</td></tr>
        <tr><td class="area">Hallways</td><td>Routine</td><td>Homestead Reports</td><td>May 2023</td></tr>
        <tr><td class="area">Laundry</td><td>Routine</td><td>Homestead Reports</td><td>May 2023</td></tr>
        <tr><td class="area">Lift</td><td>LiftWorks</td><td>Routine/Safety</td><td></td></tr>
        <tr><td class="area">Lobby/Recreation Room</td><td>Routine</td><td>Homestead Reports</td><td>May 2023</td></tr>
        <tr><td class="area">Mechanical Ventilation</td><td>Operational</td><td>AirCare FM</td><td></td></tr>
        <tr><td class="area">Pest Management</td><td>Routine</td><td>Homestead Reports</td><td>May 2023</td></tr>
        <tr><td class="area">Recreation Areas</td><td>Routine</td><td>Homestead Reports</td><td>May 2023</td></tr>
        <tr><td class="area">Pool Areas</td><td>Routine</td><td>Homestead Reports</td><td>May 2023</td></tr>
        <tr><td class="area">Roof Access</td><td>Routine</td><td>Homestead Reports</td><td>May 2023</td></tr>
        <tr><td class="area">Sauna</td><td>Routine</td><td>Homestead Reports</td><td>May 2023</td></tr>
        <tr><td class="area">Stairwell</td><td>Routine</td><td>Homestead Reports</td><td>May 2023</td></tr>
        <tr><td class="area">Tennis Court</td><td>Routine</td><td>Homestead Reports</td><td>May 2023</td></tr>
        <tr><td class="area">Washrooms</td><td>Routine</td><td>Homestead Reports</td><td>May 2023</td></tr>
      </tbody>
    </table>
    <footer class="page-foot">
      <svg width="48" height="48" viewBox="0 0 48 48" aria-hidden="true">
        <polygon points="12,6 24,18 12,30 0,18" fill="var(--green-light)"/>
        <polygon points="24,10 40,26 24,42 8,26" fill="var(--teal-dark)"/>
        <polygon points="10,32 18,40 10,48 2,40" fill="var(--green-light)"/>
      </svg>
      <div class="bar">7 Elmwick Lane Canberra City - COPYRIGHT: Homestead Reports</div>
    </footer>
  </section>

  <!-- Estimated service life -->
  <section class="page wide-page" style="left:1643px">
    <table class="data-table esl">
      <colgroup><col style="width:165px"><col style="width:38px"><col span="16"></colgroup>
      <thead>
        <tr class="caption"><th colspan="18">Estimated Service Life (ESL) Summary (indicates estimated service life of the building element and identifies anticipated next major expenditure - other than a routine service/repair)</th></tr>
        <tr><th></th><th>ESL</th><th>2022</th><th>2023</th><th>2024</th><th>2025</th><th>2026</th><th>2027</th><th>2028</th><th>2029</th><th>2030</th><th>2031</th><th>2032</th><th>2033</th><th>2034</th><th>2035</th><th>2036</th><th>2037</th></tr>
      </thead>
      <tbody>
        <tr><td colspan="18">SUPERSTRUCTURE</td></tr>
        <tr><td>Repaint Building Exterior</td><td class="num">10</td><td></td><td></td><td></td><td></td><td></td><td></td><td class="num"><span class="tick"></span></td><td></td><td></td><td></td><td></td><td></td><td></td><td></td><td></td><td></td></tr>
        <tr><td>Repaint Soffits</td><td class="num">10</td><td></td><td></td><td></td><td></td><td></td><td></td><td class="num"><span class="tick"></span></td><td></td><td></td><td></td><td></td><td></td><td></td><td></td><td></td><td></td></tr>
        <tr><td>Repair/Maintain Common Window Coverings</td><td class="num">10</td><td></td><td></td><td></td><td></td><td class="num"><span class="tick"></span></td><td></td><td></td><td></td><td></td><td></td><td></td><td></td><td></td><td></td><td></td><td></td></tr>
        <tr><td>Repair/Maintain windows</td><td class="num">5</td><td></td><td></td><td></td><td></td><td class="num"><span class="tick"></span></td><td></td><td></td><td></td><td></td><td></td><td></td><td></td><td></td><td></td><td></td><td></td></tr>
        <tr><td>Maintain Balcony/Patio/Entry Floor Tiles</td><td class="num">10</td><td></td><td></td><td></td><td></td><td class="num"><span class="tick"></span></td><td></td><td></td><td></td><td></td><td></td><td></td><td></td><td></td><td></td><td></td><td></td></tr>
        <tr><td>Repaint Balustrade &amp; Handrail Fixings</td><td class="num">20</td><td></td><td></td><td></td><td></td><td></td><td></td><td></td><td></td><td></td><td></td><td class="num"><span class="tick"></span></td><td></td><td></td><td></td><td></td><td></td></tr>
        <tr><td>Repair/Maintain Balcony Membrane</td><td class="num">5</td><td></td><td></td><td class="num"><span class="tick"></span></td><td></td><td></td><td></td><td></td><td></td><td></td><td></td><td></td><td></td><td></td><td></td><td></td><td></td></tr>
        <tr><td>Repair/Maintain Roof</td><td class="num">10</td><td></td><td></td><td></td><td></td><td></td><td></td><td class="num"><span class="tick"></span></td><td></td><td></td><td></td><td></td><td></td><td></td><td></td><td></td><td></td></tr>
        <tr><td>Repair/Maintain Skylights</td><td class="num">10</td><td></td><td></td><td class="num"><span class="tick"></span></td><td></td><td></td><td></td><td></td><td></td><td></td><td></td><td></td><td></td><td></td><td></td><td></td><td></td></tr>
        <tr><td colspan="18">&nbsp;</td></tr>
        <tr><td colspan="18">BASEMENT/CAR ACCOMODATION</td></tr>
        <tr><td>Maintain/Repair Main Garage Door Motor</td><td class="num">5</td><td></td><td></td><td></td><td class="num"><span class="tick"></span></td><td></td><td></td><td></td><td></td><td></td><td></td><td></td><td></td><td></td><td></td><td></td><td></td></tr>
      </tbody>
    </table>
    <footer class="page-foot">
      <svg width="48" height="48" viewBox="0 0 48 48" aria-hidden="true">
        <polygon points="12,6 24,18 12,30 0,18" fill="var(--green-light)"/>
        <polygon points="24,10 40,26 24,42 8,26" fill="var(--teal-dark)"/>
        <polygon points="10,32 18,40 10,48 2,40" fill="var(--green-light)"/>
      </svg>
      <div class="bar">7 Elmwick Lane Canberra City - COPYRIGHT: Homestead Reports</div>
    </footer>
  </section>

</div>
</body>
</html>
```